label design for oral care product

Kindly invite you to design bottle label (114 mm*40 mm) for our product, a kind of oral care product. The GEL is different from our previous cleanser product, as the pic we uploaded for demonstration. The color of frosted glass bottle is dark green, but the cap is white. You could download the pic of bottle among the uploaded files. The logo file and label content description are attached too. Please check them. Our product is made from many kinds of natural plant extracts, which includes herb and fruit. I wish the label would make our product look high-end and reliable. And it would be better if you could give some advice on paper material and special requirements for printing, related to your design. I value the texture of label too, because I think that stands for the quality of products. No color limitation for the use of our logo.
Target Market(s)
20-40 female, who value oral health.
Colors
Designer to choose colors to be used in the design.
Look and feel
Each slider illustrates characteristics of the customer's brand and the style your logo design should communicate.

```html
<!DOCTYPE html>
<html lang="en">
<head>
<meta charset="utf-8">
<title>Aligner Gel Label</title>
<link href="https://fonts.googleapis.com/css2?family=Lato:ital,wght@0,300;0,400;0,700;0,900;1,400&display=swap" rel="stylesheet">
<style>
  :root{
    --page:#e9e9e6;
    --paper:#ffffff;
    --edge:#c3c83a;
    --frame:#9aa638;
    --sage:#b7c4a2;
    --band-line:#4e6a2a;
    --olive-dark:#566c2c;
    --olive:#6b8142;
    --olive-soft:#87996a;
    --text-green:#5b7a2c;
    --ink:#1d1d1b;
    --white:#ffffff;
  }
  *{box-sizing:border-box;margin:0;padding:0}
  html,body{width:862px;height:1200px;overflow:hidden;background:var(--page);font-family:"Lato",sans-serif}
  .canvas{position:relative;width:862px;height:1200px}
  .label{
    position:absolute;left:31px;top:457px;width:928px;height:332px;
    transform:scale(0.862);transform-origin:0 0;
    background:var(--paper);border:2px solid var(--edge);
    box-shadow:0 6px 14px rgba(0,0,0,.25);
  }
  .label__frame{position:absolute;inset:8px;border:1px solid var(--frame);pointer-events:none;z-index:3}
  .label__pattern{position:absolute;left:0;top:0;width:100%;height:80px;
    background:linear-gradient(90deg,#b3c19d,#bccaa8 50%,#b3c19d)}
  .label__rule{position:absolute;left:0;top:80px;width:100%;height:4px;background:var(--band-line)}
  .front{position:absolute;left:350px;top:40px;width:228px;height:252px;
    background:linear-gradient(180deg,var(--olive-dark),var(--olive) 70%);z-index:2;border-radius:2px;overflow:hidden}
  .brand{display:flex;align-items:center;justify-content:center;gap:6px;margin-top:22px;
    color:var(--white);font-weight:900;font-size:25px;letter-spacing:.5px}
  .brand__dot{width:10px;height:10px;border:2px solid var(--white);border-radius:50%}
  .product{margin-top:20px;text-align:center;color:var(--white);font-size:33px;line-height:1;letter-spacing:.5px}
  .product b{font-weight:900}
  .product span{font-weight:300}
  .tagline{text-align:center;color:var(--white);font-size:13px;line-height:16px;margin-top:6px}
  .solution{position:absolute;left:0;bottom:0;width:100%;height:78px;background:var(--olive-soft);padding:9px 0 0 14px;color:#eef1e6;font-style:italic;font-size:12px}
  .solution li{list-style:none;display:flex;gap:6px;margin-top:3px;line-height:14px}
  .solution li svg{flex:none;margin-top:2px}
  .solution ul{width:130px}
  .drop{position:absolute;right:14px;bottom:6px;width:66px;height:84px}
  .volume{position:absolute;left:350px;width:228px;top:294px;text-align:center;font-size:12px;color:var(--ink);z-index:2}
  .side{position:absolute;top:108px;color:var(--text-green);font-size:16px;line-height:18px}
  .side h2{font-size:16px;font-weight:700;margin-bottom:6px}
  .directions{left:75px;width:230px}
  .directions li{list-style:none;display:flex;gap:6px;margin-bottom:6px}
  .directions li svg{flex:none;margin-top:3px}
  .origin{margin-top:12px;color:var(--ink);font-size:15px;line-height:18px;letter-spacing:.5px}
  .origin b{font-weight:700}
  .contains{left:653px;width:250px}
  .contains .intro{font-weight:300;margin-bottom:4px}
  .contains .intro strong{font-weight:700}
  .contains li{list-style:none;display:flex;gap:6px;align-items:center;line-height:19.5px}
</style>
</head>
<body>
<div class="canvas">
  <div class="label">
    <div class="label__pattern" role="img" aria-label="Faint botanical line pattern of herbs and flowers"></div>
    <div class="label__rule"></div>
    <div class="label__frame"></div>

    <section class="side directions">
      <h2>DIRECTIONS:</h2>
      <ul>
        <li><svg width="8" height="12" viewBox="0 0 8 12"><path d="M4 0C4 0 0 6 0 8a4 4 0 0 0 8 0C8 6 4 0 4 0Z" fill="var(--text-green)"/></svg><span>Drop on the teeth directly after brushing.</span></li>
        <li><svg width="8" height="12" viewBox="0 0 8 12"><path d="M4 0C4 0 0 6 0 8a4 4 0 0 0 8 0C8 6 4 0 4 0Z" fill="var(--text-green)"/></svg><span>Or, put into clear aligners before wearing again.</span></li>
        <li><svg width="8" height="12" viewBox="0 0 8 12"><path d="M4 0C4 0 0 6 0 8a4 4 0 0 0 8 0C8 6 4 0 4 0Z" fill="var(--text-green)"/></svg><span>No need to rinse your mouth with water.</span></li>
      </ul>
      <p class="origin">MADE IN<br><b>TAIWAN</b></p>
    </section>

    <section class="front">
      <div class="brand"><span>Leafwell</span><span class="brand__dot"></span></div>
      <h1 class="product"><b>ALIGNER</b> <span>GEL</span></h1>
      <p class="tagline">IMMUNE SUPPORT<br>For Oral Health</p>
      <div class="solution">
        <p>The Solution to:</p>
        <ul>
          <li><svg width="10" height="10" viewBox="0 0 10 10"><circle cx="5" cy="5" r="5" fill="#eef1e6"/><path d="M2.6 5.2l1.7 1.6 3.2-3.4" stroke="var(--olive-soft)" stroke-width="1.5" fill="none"/></svg><span>Maintain Dental Hygiene.</span></li>
          <li><svg width="10" height="10" viewBox="0 0 10 10"><circle cx="5" cy="5" r="5" fill="#eef1e6"/><path d="M2.6 5.2l1.7 1.6 3.2-3.4" stroke="var(--olive-soft)" stroke-width="1.5" fill="none"/></svg><span>Strengthen Gums</span></li>
        </ul>
        <svg class="drop" viewBox="0 0 66 84" role="img" aria-label="Water drop illustration holding a tooth and a green leaf">
          <defs><radialGradient id="dropFill" cx="50%" cy="60%" r="60%"><stop offset="0" stop-color="#d9e6c4"/><stop offset="1" stop-color="#7fa14a"/></radialGradient></defs>
          <path d="M33 0C33 0 2 42 2 55a31 29 0 0 0 62 0C64 42 33 0 33 0Z" fill="url(#dropFill)"/>
        </svg>
      </div>
    </section>
    <p class="volume">30ml(1fl oz)</p>

    <section class="side contains">
      <p class="intro"><strong>CONTAINS:</strong> A proprietary blend of natural plant extract including:</p>
      <ul>
        <li><svg width="9" height="10" viewBox="0 0 9 10"><path d="M0 10C0 4 3 0 9 0C9 6 6 10 0 10Z" fill="var(--text-green)"/></svg>Angelica.</li>
        <li><svg width="9" height="10" viewBox="0 0 9 10"><path d="M0 10C0 4 3 0 9 0C9 6 6 10 0 10Z" fill="var(--text-green)"/></svg>Radix Rehmanniae.</li>
        <li><svg width="9" height="10" viewBox="0 0 9 10"><path d="M0 10C0 4 3 0 9 0C9 6 6 10 0 10Z" fill="var(--text-green)"/></svg>Coptis.</li>
        <li><svg width="9" height="10" viewBox="0 0 9 10"><path d="M0 10C0 4 3 0 9 0C9 6 6 10 0 10Z" fill="var(--text-green)"/></svg>Honeysuckle.</li>
        <li><svg width="9" height="10" viewBox="0 0 9 10"><path d="M0 10C0 4 3 0 9 0C9 6 6 10 0 10Z" fill="var(--text-green)"/></svg>Echinacea.</li>
        <li><svg width="9" height="10" viewBox="0 0 9 10"><path d="M0 10C0 4 3 0 9 0C9 6 6 10 0 10Z" fill="var(--text-green)"/></svg>Sage.</li>
        <li><svg width="9" height="10" viewBox="0 0 9 10"><path d="M0 10C0 4 3 0 9 0C9 6 6 10 0 10Z" fill="var(--text-green)"/></svg>Chamomile.</li>
        <li><svg width="9" height="10" viewBox="0 0 9 10"><path d="M0 10C0 4 3 0 9 0C9 6 6 10 0 10Z" fill="var(--text-green)"/></svg>Acerola cherry.</li>
      </ul>
    </section>
  </div>
</div>
</body>
</html>
```